Creative way to lay out a career advancement graphic

Are you a designer with a knack for turning complex concepts into visually captivating masterpieces? We have an exciting project that needs your unique talent! We're on the lookout for a creative designer to help us visualize our company's diverse career paths. Our organization offers a plethora of opportunities in project management, engineering, sales, and more. We want to showcase these pathways in a visually engaging manner to empower potential job candidates with a clear understanding of their advancement options within our company. Design must be flexible and able to be edited.

Check out the attached examples of the positions we'd like to include in this visualization (doc "inside sales" are correct positions). Your task will be to transform this information into a visually stunning representation that's both informative and inspiring.
This project is not just about design—it's about shaping the narrative of career growth and opportunity within our organization. Your creative input will play a vital role in helping us attract top talent and communicate our company's commitment to fostering professional development. Brand guidelines are also attached for reference. The document titled "parvel" demonstrates a badly done version of what we are trying to achieve. We want to denote multiple routes of advancement. You don't have to get the paths completely correct, you just need to show how it could be approached in a design. For example, A "submittal Specialist" could become a "project manager" but also could ascend to the role of "Industrial Estimator" if they want to move in that direction.

```html
<!DOCTYPE html>
<html lang="en">
<head>
<meta charset="utf-8">
<title>Corvane Sales Development</title>
<link href="https://fonts.googleapis.com/css2?family=Arimo:wght@700&family=Bebas+Neue&family=Carlito&display=swap" rel="stylesheet">
<style>
  :root{
    --navy:#020263;
    --gold:#f5a800;
    --line:#5a5ac4;
    --bubble:#5656b0;
    --white:#ffffff;
  }
  html,body{margin:0;padding:0;overflow:hidden;background:#ffffff;}
  .poster{
    position:relative;width:1046px;height:1200px;box-sizing:border-box;
    background:var(--navy);border:20px solid var(--gold);overflow:hidden;
    font-family:"Carlito",sans-serif;color:var(--white);
  }
  .header-rule{position:absolute;left:43px;width:920px;height:2px;background:var(--line);}
  .header-rule.top{top:32px;}
  .header-rule.bottom{top:130px;}
  .brand{position:absolute;left:43px;top:58px;}
  .brand-name{display:flex;align-items:center;gap:8px;font-family:"Arimo",sans-serif;font-weight:700;font-size:38px;line-height:1;color:var(--white);letter-spacing:0.5px;}
  .brand-dot{width:26px;height:26px;border-radius:50%;background:var(--gold);}
  .brand-tagline{font-family:"Carlito",sans-serif;font-size:13px;margin-top:6px;color:var(--white);}
  .page-title{position:absolute;right:43px;top:44px;margin:0;font-family:"Bebas Neue",sans-serif;font-weight:400;font-size:78px;line-height:1;letter-spacing:7px;color:var(--white);}
  .page-title .accent{color:var(--gold);}
  .paths{position:absolute;left:-20px;top:-20px;width:1046px;height:1200px;}
  .role{position:absolute;width:300px;text-align:center;}
  .role-title{margin:0 0 5px;font-family:"Arimo",sans-serif;font-weight:700;font-size:19px;line-height:24px;color:var(--gold);}
  .role-duties{margin:0;padding:0;list-style:none;font-size:12.5px;line-height:17px;}
</style>
</head>
<body>
<main class="poster">
  <div class="header-rule top"></div>
  <div class="brand">
    <div class="brand-name"><span class="brand-dot"></span>CORVANE</div>
    <div class="brand-tagline">Power Systems for Industry</div>
  </div>
  <h1 class="page-title">Sales <span class="accent">Development</span></h1>
  <div class="header-rule bottom"></div>

  <svg class="paths" viewBox="0 0 1046 1200" aria-hidden="true">
    <g fill="none" stroke="var(--line)" stroke-width="1.6">
      <path d="M115,200 H90 Q65,200 65,225 V410 Q65,430 82,430"/>
      <path d="M297,200 H337 Q357,200 357,222 V300 Q357,320 379,320 H628 Q650,320 650,298 V222 Q650,200 672,200 H719"/>
      <path d="M357,370 V508 M673,370 V508"/>
      <path d="M959,370 Q983,380 983,410 V485 Q983,505 960,505 H90 Q65,505 65,530 Q65,550 86,555"/>
      <path d="M355,565 V700 M672,565 V700"/>
      <path d="M941,574 Q983,577 983,610 V685 Q983,705 960,705 H90 Q65,705 65,730 Q65,755 86,760"/>
      <path d="M318,762 H355 Q383,762 383,790 V860 Q383,880 405,880 H960 Q983,880 983,860 V790 Q983,762 941,762"/>
      <path d="M681,742 V858"/>
    </g>
    <g fill="var(--line)">
      <circle cx="115" cy="200" r="3"/><circle cx="297" cy="200" r="3"/><circle cx="719" cy="200" r="3"/><circle cx="82" cy="430" r="3"/>
      <circle cx="357" cy="370" r="3"/><circle cx="357" cy="508" r="3"/><circle cx="673" cy="370" r="3"/><circle cx="673" cy="508" r="3"/><circle cx="959" cy="370" r="3"/>
      <circle cx="355" cy="565" r="3"/><circle cx="355" cy="700" r="3"/><circle cx="672" cy="565" r="3"/><circle cx="672" cy="700" r="3"/><circle cx="86" cy="555" r="3"/><circle cx="941" cy="574" r="3"/>
      <circle cx="318" cy="762" r="3"/><circle cx="86" cy="760" r="3"/><circle cx="941" cy="762" r="3"/><circle cx="681" cy="742" r="3"/><circle cx="681" cy="858" r="3"/>
      <polygon points="60,300 70,300 65,292"/>
      <polygon points="352,260 362,260 357,268"/>
      <polygon points="496,315 496,325 504,320"/>
      <polygon points="645,270 655,270 650,262"/>
      <polygon points="978,440 988,440 983,432"/>
      <polygon points="476,500 476,510 484,505"/>
      <polygon points="806,500 806,510 814,505"/>
      <polygon points="60,535 70,535 65,527"/>
      <polygon points="978,655 988,655 983,647"/>
      <polygon points="476,700 476,710 484,705"/>
      <polygon points="806,700 806,710 814,705"/>
      <polygon points="60,735 70,735 65,727"/>
      <polygon points="378,825 388,825 383,817"/>
      <polygon points="978,818 988,818 983,826"/>
      <polygon points="692,875 692,885 684,880"/>
      <polygon points="353,434 353,444 347,439"/><polygon points="361,434 361,444 367,439"/>
      <polygon points="669,434 669,444 663,439"/><polygon points="677,434 677,444 683,439"/>
      <polygon points="351,627 351,637 345,632"/><polygon points="359,627 359,637 365,632"/>
      <polygon points="668,627 668,637 662,632"/><polygon points="676,627 676,637 682,632"/>
      <polygon points="677,795 677,805 671,800"/><polygon points="685,795 685,805 691,800"/>
    </g>

    <g>
      <rect x="65" y="1045" width="160" height="70" rx="12" fill="var(--gold)"/>
      <text x="145" y="1097" text-anchor="middle" font-family="Arimo,sans-serif" font-weight="700" font-size="46" fill="var(--navy)">DATA</text>
      <path d="M232,1080 H358" stroke="var(--white)" stroke-width="1.4" stroke-dasharray="5 4" fill="none"/>
      <ellipse cx="440" cy="1080" rx="78" ry="46" fill="var(--bubble)"/>
      <text x="440" y="1087" text-anchor="middle" font-family="Arimo,sans-serif" font-weight="700" font-size="20" fill="var(--white)">Condition?</text>
      <path d="M526,1080 H540 M576,1080 H596" stroke="var(--white)" stroke-width="1.4" stroke-dasharray="5 4" fill="none"/>
      <text x="558" y="1086" text-anchor="middle" font-family="Arimo,sans-serif" font-weight="700" font-size="16" fill="var(--white)">No</text>
      <polygon points="598,1073 598,1087 606,1080" fill="var(--gold)"/>
      <circle cx="690" cy="1080" r="80" fill="none" stroke="var(--white)" stroke-width="2" stroke-dasharray="1.5 4"/>
      <circle cx="690" cy="1080" r="73" fill="var(--bubble)"/>
      <text x="690" y="1091" text-anchor="middle" font-family="Arimo,sans-serif" font-weight="700" font-size="30" fill="var(--white)">Process</text>
      <path d="M776,1080 H812" stroke="var(--white)" stroke-width="1.4" stroke-dasharray="5 4" fill="none"/>
      <polygon points="814,1073 814,1087 822,1080" fill="var(--gold)"/>
      <circle cx="905" cy="1080" r="80" fill="none" stroke="var(--white)" stroke-width="2" stroke-dasharray="1.5 4"/>
      <circle cx="905" cy="1080" r="73" fill="var(--bubble)"/>
      <text x="905" y="1091" text-anchor="middle" font-family="Arimo,sans-serif" font-weight="700" font-size="30" fill="var(--white)">Process</text>
      <path d="M450,1030 Q520,960 600,950 M640,950 Q760,955 830,1002" stroke="var(--white)" stroke-width="1.2" stroke-dasharray="5 4" fill="none"/>
      <text x="620" y="957" text-anchor="middle" font-family="Arimo,sans-serif" font-weight="700" font-size="15" fill="var(--white)">Yes</text>
      <polygon points="828,1010 838,1000 838,1012" fill="var(--gold)"/>
    </g>
  </svg>

  <section class="role" style="left:39px;top:158px;">
    <h2 class="role-title">Outside Sales</h2>
    <ul class="role-duties"><li>Prospecting and lead generation</li><li>Building and maintaining relationships</li><li>Closing sales and achieving targets</li></ul>
  </section>
  <section class="role" style="left:330px;top:158px;">
    <h2 class="role-title">Sales Leadership</h2>
    <ul class="role-duties"><li>Sales sets goals and targets</li><li>Sales team supervision, mentoring,</li><li>training and coaching</li><li>Sales strategy development and</li><li>implementation</li></ul>
  </section>
  <section class="role" style="left:668px;top:158px;">
    <h2 class="role-title">Vice President, Sales</h2>
    <ul class="role-duties"><li>Sales strategy development</li><li>Revenue generation</li><li>Market analysis</li><li>Sales forecasting and budgeting</li><li>Team Leadership</li></ul>
  </section>

  <section class="role" style="left:40px;top:328px;">
    <h2 class="role-title">Lead Project Manager</h2>
    <ul class="role-duties"><li>Team leadership, mentoring and training</li><li>Project planning and organization</li><li>Monitoring and control</li><li>Customer service and communication</li><li>Continuous improvement</li></ul>
  </section>
  <section class="role" style="left:345px;top:328px;">
    <h2 class="role-title">Lead Technical Engineer</h2>
    <ul class="role-duties"><li>Team leadership, mentoring and training</li><li>Technical sales liaison</li><li>Influence specifications</li><li>Read &amp; interpret specifications</li></ul>
  </section>
  <section class="role" style="left:652px;top:328px;">
    <h2 class="role-title">Lead Project Engineer</h2>
    <ul class="role-duties"><li>Team leadership, mentoring and training</li><li>Technical expertise + engineering support</li><li>Subject matter expert relating to job,</li><li>equipment and commissioning</li><li>Quality control and project execution</li><li>Continuous improvement</li></ul>
  </section>

  <section class="role" style="left:34px;top:542px;">
    <h2 class="role-title">Project Manager</h2>
    <ul class="role-duties"><li>Project planning and organization</li><li>Monitoring and control</li><li>Customer service and communication</li></ul>
  </section>
  <section class="role" style="left:341px;top:518px;">
    <h2 class="role-title">Industrial<br>Estimator (Senior)</h2>
    <ul class="role-duties"><li>Quote preparation for more complex jobs</li><li>Specification and drawing review</li><li>Customer and vendor relationship</li><li>Analyze competitive pricing</li><li>Support outside sales</li></ul>
  </section>
  <section class="role" style="left:660px;top:542px;">
    <h2 class="role-title">Project Engineer</h2>
    <ul class="role-duties"><li>Technical expertise + engineering Support</li><li>Subject matter expert relating to job,</li><li>equipment and commissioning</li><li>Quality control and project execution</li></ul>
  </section>

  <section class="role" style="left:34px;top:712px;">
    <h2 class="role-title">Industrial<br>Estimator (Junior)</h2>
    <ul class="role-duties"><li>Quote preparation for less complex jobs</li><li>Specification and drawing Review</li><li>Vendor relationship</li><li>Support outside sales</li></ul>
  </section>
  <section class="role" style="left:366px;top:712px;">
    <h2 class="role-title">Submittal<br>Specialist</h2>
    <ul class="role-duties"><li>Document control and management</li><li>Submittal preparation and review</li><li>Communication and coordination</li></ul>
  </section>
  <section class="role" style="left:660px;top:712px;">
    <h2 class="role-title">Project Coordinator<br>(Gatekeeper)</h2>
    <ul class="role-duties"><li>Data entry for projects</li><li>Reviews project complexity</li><li>and assigns accordingly</li></ul>
  </section>
</main>
</body>
</html>
```